UI design for a mobile app that manages color schemes/pallettes

Should look cool, different, and modern.
The UI colors should not compete with pallette colors (as much as possible)
Features:
Currently looking for 3 pages/screens for the app: Browse through all palettes, view/edit a single palette, import
Features to include in the UI:
- View the list of color palettes (each list item includes a preview showing all colors in that color palette)
- View a particular color palette.
- Each displayed color should show:
- hex value
- rgb(255, 255, 255) value
- Name of pallete
- Button to copy the palette to a new pallette
- Sliders to change the properties (hue, saturation, value) or all colors in the palette at once
- Ability to add color
- Ability to remove color
- Switch background color that the pallete is displayed on: (black, mid gray, white, custom)
- A page that allows you to import palettes from a folder
Look and feel
Each slider illustrates characteristics of the customer's brand and the style your logo design should communicate.

```html
<!DOCTYPE html>
<html lang="en">
<head>
<meta charset="utf-8">
<title>Palette Manager – App Screens</title>
<link rel="stylesheet" href="https://fonts.googleapis.com/css2?family=Poppins:wght@400;500;600&display=swap">
<style>
:root{
  --bg:#eef0f4;
  --screen:#f9f9fa;
  --ink:#2a2b30;
  --muted:#a9abb2;
  --line:#e7e8ec;
  --white:#ffffff;
  --accent-add:#f2385f;
  --accent-ok:#5fcf1c;
  --c-charcoal:#50514f;
  --c-coral:#f25f5c;
  --c-sun:#ffe066;
  --c-ocean:#247ba0;
  --c-mint:#70c1b3;
  --c-gold:#ffca3a;
}
*{box-sizing:border-box;margin:0;padding:0}
html,body{width:1182px;height:1200px;overflow:hidden;background:var(--bg);font-family:"Poppins",sans-serif;color:var(--ink)}
.board{display:grid;grid-template-columns:repeat(3,340px);grid-template-rows:repeat(2,555px);gap:30px 40px;padding:30px 41px}
.screen{background:var(--screen);border-radius:42px;box-shadow:0 18px 40px rgba(60,70,100,.14),0 2px 6px rgba(60,70,100,.06);padding:34px 22px 18px;display:flex;flex-direction:column;position:relative;overflow:hidden}
/* palette bands */
.bands{display:flex;flex-direction:column;gap:8px;flex:1}
.band{flex:1;border-radius:10px;display:flex;align-items:center;justify-content:space-between;padding:0 16px;color:var(--white);font-weight:500;font-size:15px;letter-spacing:.5px}
.band .tools{display:flex;gap:12px}
.band svg{width:15px;height:15px;stroke:currentColor;fill:none;stroke-width:1.5}
/* bottom bar */
.bottom-bar{display:flex;align-items:center;gap:16px;margin-top:16px}
.pill{background:var(--white);border-radius:14px;padding:7px 14px;font-size:10px;font-weight:500;box-shadow:0 4px 12px rgba(90,100,160,.12)}
.bottom-bar .spacer{flex:1}
.bottom-bar svg{width:17px;height:17px;stroke:var(--ink);fill:none;stroke-width:1.5}
.menu-btn{width:34px;height:34px;border-radius:10px;background:var(--white);display:grid;place-items:center;box-shadow:0 4px 12px rgba(90,100,160,.14)}
/* search */
.search{display:flex;align-items:center;gap:10px;background:#f1f2f4;border-radius:16px;padding:9px 14px;font-size:10px;color:var(--muted);margin-bottom:16px}
.search svg{width:15px;height:15px;stroke:var(--ink);fill:none;stroke-width:1.8}
/* palette list */
.list{display:flex;flex-direction:column;gap:10px;flex:1}
.row{display:flex;flex-direction:column;gap:3px}
.strip{display:flex;height:62px;border-radius:10px;overflow:hidden}
.strip span{flex:1}
.dots{align-self:flex-end;font-size:12px;line-height:8px;letter-spacing:1px;font-weight:600}
/* context menu */
.ctx{position:absolute;left:18px;right:18px;bottom:18px;height:230px;border-radius:26px;background:linear-gradient(135deg,rgba(214,222,248,.92),rgba(252,244,246,.93) 45%,rgba(214,236,238,.93) 70%,rgba(253,226,196,.95));backdrop-filter:blur(6px);padding:28px 26px;display:flex;flex-direction:column;justify-content:space-around;box-shadow:0 12px 30px rgba(80,90,130,.18)}
.ctx-item{display:flex;justify-content:space-between;align-items:center;font-size:13px;font-weight:500}
.ctx-item svg{width:17px;height:17px;stroke:var(--ink);fill:none;stroke-width:1.6}
/* shades */
.shades{flex:1;display:flex;flex-direction:column;border-radius:4px;overflow:hidden}
.shades span{flex:1;display:flex;align-items:center;justify-content:center;font-size:10px;color:var(--white);font-weight:500;gap:8px}
.shades .dot{width:6px;height:6px;border-radius:50%;background:rgba(255,255,255,.7)}
/* color detail */
.back{width:20px;height:20px;stroke:var(--ink);fill:none;stroke-width:1.6;margin:0 0 14px 4px}
.detail{flex:1;background:var(--c-gold);border-radius:6px;display:flex;flex-direction:column;padding:24px 30px 0;color:var(--white);position:relative;overflow:hidden}
.spec{border-bottom:1px solid rgba(255,255,255,.35);padding:9px 0 10px}
.spec small{display:block;font-size:9px;color:rgba(255,255,255,.75)}
.spec b{font-weight:500;font-size:17px;letter-spacing:.5px}
.copied{display:flex;flex-direction:column;align-items:center;margin-top:18px;font-size:9px;color:rgba(255,255,255,.8);gap:4px}
.copied svg{width:32px;height:32px;stroke:var(--white);fill:none;stroke-width:2.2}
.steps{position:absolute;left:0;right:0;bottom:0;height:62px;display:flex}
.steps span{flex:1}
/* editor */
.mini{display:flex;height:64px;border-radius:10px;overflow:hidden;margin-bottom:10px}
.mini span{flex:1;font-size:7.5px;color:var(--white);display:flex;align-items:flex-end;justify-content:center;padding-bottom:8px;font-weight:500}
.adjust{flex:1;background:linear-gradient(150deg,#ffffff,#eaf4f3 55%,#f4eee6);border-radius:22px;padding:18px 20px;display:flex;flex-direction:column;gap:13px;box-shadow:0 8px 24px rgba(80,90,130,.1)}
.slider label{display:flex;justify-content:space-between;font-size:10px;font-weight:500;margin-bottom:6px}
.slider label em{font-style:normal;font-size:8px;color:var(--muted)}
.track{height:5px;border-radius:3px;position:relative}
.knob{position:absolute;top:-5px;width:15px;height:15px;border-radius:50%;background:var(--white);box-shadow:0 1px 4px rgba(0,0,0,.25)}
.track.hue{background:linear-gradient(90deg,#f4403a,#f9d423,#3fd93b,#26c6da,#3b52f5,#d42bd9)}
.track.sat{background:linear-gradient(90deg,#e8dede,#d53a44)}
.track.bri{background:linear-gradient(90deg,#151515,#c9cccc)}
.track.temp{background:linear-gradient(90deg,#3d63df,#c8d2e6,#e7a45a)}
.actions{display:flex;justify-content:flex-end;gap:12px;margin-top:4px}
.fab{width:38px;height:38px;border-radius:50%;display:grid;place-items:center;box-shadow:0 6px 14px rgba(0,0,0,.18)}
.fab svg{width:16px;height:16px;stroke:var(--white);fill:none;stroke-width:2.4}
.fab.add{background:var(--accent-add)}
.fab.ok{background:var(--accent-ok)}
</style>
</head>
<body>
<svg width="0" height="0" style="position:absolute">
  <defs>
    <symbol id="i-grid" viewBox="0 0 16 16"><rect x="2" y="2" width="5" height="5" rx="1"/><rect x="9" y="2" width="5" height="5" rx="1"/><rect x="2" y="9" width="5" height="5" rx="1"/><rect x="9" y="9" width="5" height="5" rx="1"/></symbol>
    <symbol id="i-copy" viewBox="0 0 16 16"><rect x="3" y="5" width="9" height="9" rx="1.5"/><path d="M6 5V3h7v8h-1"/></symbol>
    <symbol id="i-lock" viewBox="0 0 16 16"><rect x="3" y="7" width="10" height="7" rx="1.5"/><path d="M5 7V5a3 3 0 0 1 6 0"/></symbol>
    <symbol id="i-sun" viewBox="0 0 18 18"><circle cx="9" cy="9" r="3"/><path d="M9 1.5v2M9 14.5v2M1.5 9h2M14.5 9h2M3.7 3.7l1.4 1.4M12.9 12.9l1.4 1.4M3.7 14.3l1.4-1.4M12.9 5.1l1.4-1.4"/></symbol>
    <symbol id="i-export" viewBox="0 0 18 18"><path d="M8 3H3v12h12v-5"/><path d="M10 2h6v6M16 2 8 10"/></symbol>
    <symbol id="i-heart" viewBox="0 0 18 18"><path d="M9 15.5S2.5 11.5 2.5 6.8A3.3 3.3 0 0 1 9 5.3a3.3 3.3 0 0 1 6.5 1.5C15.5 11.5 9 15.5 9 15.5z"/></symbol>
    <symbol id="i-menu" viewBox="0 0 16 16"><path d="M3 4h10M3 8h10M3 12h10"/></symbol>
    <symbol id="i-search" viewBox="0 0 16 16"><circle cx="7" cy="7" r="4.5"/><path d="m10.5 10.5 3 3"/></symbol>
    <symbol id="i-link" viewBox="0 0 18 18"><path d="M7.5 10.5a3 3 0 0 0 4.2 0l2.5-2.5a3 3 0 0 0-4.2-4.2L9 4.8"/><path d="M10.5 7.5a3 3 0 0 0-4.2 0L3.8 10a3 3 0 0 0 4.2 4.2l1-1"/></symbol>
  </defs>
</svg>

<main class="board">

  <!-- Single palette -->
  <section class="screen palette-view">
    <div class="bands">
      <div class="band" style="background:var(--c-charcoal)">50514F<div class="tools"><svg><use href="#i-grid"/></svg><svg><use href="#i-copy"/></svg><svg><use href="#i-lock"/></svg></div></div>
      <div class="band" style="background:var(--c-coral)">F25F5C<div class="tools"><svg><use href="#i-grid"/></svg><svg><use href="#i-copy"/></svg><svg><use href="#i-lock"/></svg></div></div>
      <div class="band" style="background:var(--c-sun)">FFE066<div class="tools"><svg><use href="#i-grid"/></svg><svg><use href="#i-copy"/></svg><svg><use href="#i-lock"/></svg></div></div>
      <div class="band" style="background:var(--c-ocean)">247BA0<div class="tools"><svg><use href="#i-grid"/></svg><svg><use href="#i-copy"/></svg><svg><use href="#i-lock"/></svg></div></div>
      <div class="band" style="background:var(--c-mint)">70C1B3<div class="tools"><svg><use href="#i-grid"/></svg><svg><use href="#i-copy"/></svg><svg><use href="#i-lock"/></svg></div></div>
    </div>
    <div class="bottom-bar">
      <span class="pill">More pallettes</span><span class="spacer"></span>
      <svg><use href="#i-sun"/></svg><svg><use href="#i-export"/></svg><svg><use href="#i-heart"/></svg>
      <span class="menu-btn"><svg><use href="#i-menu"/></svg></span>
    </div>
  </section>

  <!-- Browse palettes -->
  <section class="screen browse">
    <div class="search"><svg><use href="#i-search"/></svg>Search color or topics...</div>
    <div class="list">
      <div class="row"><div class="strip"><span style="background:#152b3c"></span><span style="background:#266e7a"></span><span style="background:#f8e8d4"></span><span style="background:#f5841f"></span><span style="background:#7f3926"></span></div><span class="dots">···</span></div>
      <div class="row"><div class="strip"><span style="background:#877426"></span><span style="background:#bbc09a"></span><span style="background:#f9d5c5"></span><span style="background:#f29a1e"></span><span style="background:#e66f35"></span></div><span class="dots">···</span></div>
      <div class="row"><div class="strip"><span style="background:#f9676b"></span><span style="background:#f6c244"></span><span style="background:#8dcb3a"></span><span style="background:#2888c8"></span><span style="background:#6f5a9e"></span></div><span class="dots">···</span></div>
      <div class="row"><div class="strip"><span style="background:#313e80"></span><span style="background:#8896ef"></span><span style="background:#f2c357"></span><span style="background:#f3e4ea"></span><span style="background:#f08fae"></span></div><span class="dots">···</span></div>
      <div class="row"><div class="strip"><span style="background:#8fc9e2"></span><span style="background:#2fa0bf"></span><span style="background:#113e57"></span><span style="background:#f4b31b"></span><span style="background:#f28b1c"></span></div><span class="dots">···</span></div>
    </div>
  </section>

  <!-- Browse with palette menu -->
  <section class="screen browse">
    <div class="search"><svg><use href="#i-search"/></svg>Search color or topics...</div>
    <div class="list">
      <div class="row"><div class="strip"><span style="background:#152b3c"></span><span style="background:#266e7a"></span><span style="background:#f8e8d4"></span><span style="background:#f5841f"></span><span style="background:#7f3926"></span></div><span class="dots">···</span></div>
      <div class="row"><div class="strip"><span style="background:#877426"></span><span style="background:#bbc09a"></span><span style="background:#f9d5c5"></span><span style="background:#f29a1e"></span><span style="background:#e66f35"></span></div><span class="dots">···</span></div>
      <div class="row"><div class="strip"><span style="background:#f9676b"></span><span style="background:#f6c244"></span><span style="background:#8dcb3a"></span><span style="background:#2888c8"></span><span style="background:#6f5a9e"></span></div><span class="dots">···</span></div>
      <div class="row"><div class="strip"><span style="background:#313e80"></span><span style="background:#8896ef"></span><span style="background:#f2c357"></span><span style="background:#f3e4ea"></span><span style="background:#f08fae"></span></div></div>
    </div>
    <div class="ctx">
      <div class="ctx-item">Explore more<svg><use href="#i-search"/></svg></div>
      <div class="ctx-item">Copy palette<svg><use href="#i-link"/></svg></div>
      <div class="ctx-item">Export palette<svg><use href="#i-export"/></svg></div>
      <div class="ctx-item">Add to favorite<svg><use href="#i-heart"/></svg></div>
    </div>
  </section>

  <!-- Shades of one colour -->
  <section class="screen shade-view">
    <div class="shades">
      <span style="background:#fdf6dc"></span><span style="background:#fcefbd"></span><span style="background:#fbe79d"></span><span style="background:#f9df7c"></span><span style="background:#f8d75a"></span><span style="background:#f6cf35"></span>
      <span style="background:#f5c400"><i class="dot"></i>F5C400</span>
      <span style="background:#ddb110"></span><span style="background:#c29c18"></span><span style="background:#a5871c"></span><span style="background:#86701e"></span><span style="background:#675a1e"></span><span style="background:#48411b"></span><span style="background:#2f2c17"></span><span style="background:#1e1d14"></span>
    </div>
    <div class="bottom-bar">
      <span class="pill">More pallettes</span><span class="spacer"></span>
      <svg><use href="#i-sun"/></svg><svg><use href="#i-export"/></svg><svg><use href="#i-heart"/></svg>
      <span class="menu-btn"><svg><use href="#i-menu"/></svg></span>
    </div>
  </section>

  <!-- Colour detail -->
  <section class="screen color-detail">
    <svg class="back" viewBox="0 0 20 20"><path d="M16 10H4M9 5l-5 5 5 5"/></svg>
    <div class="detail">
      <div class="spec"><small>Hex</small><b>FFCA3A</b></div>
      <div class="spec"><small>RGB</small><b>255, 202, 58</b></div>
      <div class="spec"><small>CMYK</small><b>0, 21, 88, 0</b></div>
      <div class="spec"><small>LAB</small><b>84, 10, 74</b></div>
      <div class="copied"><svg viewBox="0 0 32 32"><path d="M27 14a11 11 0 1 1-6-9"/><path d="m10 15 5 5 12-12"/></svg>Copied</div>
      <div class="steps"><span style="background:#f9676b"></span><span style="background:#8dcb3a"></span><span style="background:#2888c8"></span><span style="background:#6f5a9e"></span></div>
    </div>
  </section>

  <!-- Palette editor -->
  <section class="screen editor">
    <div class="mini"><span style="background:#264653">264653</span><span style="background:#2a9d8f">2A9D8F</span><span style="background:#e9c46a">E9C46A</span><span style="background:#f4a261">F4A261</span><span style="background:#e76f51">E76F51</span></div>
    <div class="mini"><span style="background:#243518">243518</span><span style="background:#55621b">55621B</span><span style="background:#b81cb6">B81CB6</span><span style="background:#9b0dca">9B0DCA</span><span style="background:#6217ad">6217AD</span></div>
    <div class="adjust">
      <div class="slider"><label>Hue<em>-51</em></label><div class="track hue"><i class="knob" style="left:36%"></i></div></div>
      <div class="slider"><label>Saturation<em>0</em></label><div class="track sat"><i class="knob" style="left:48%"></i></div></div>
      <div class="slider"><label>Brightness<em>-37</em></label><div class="track bri"><i class="knob" style="left:30%"></i></div></div>
      <div class="slider"><label>Temperature<em>0</em></label><div class="track temp"><i class="knob" style="left:48%"></i></div></div>
      <div class="actions">
        <span class="fab ok"><svg viewBox="0 0 16 16"><path d="m3 8 3.5 3.5L13 5"/></svg></span>
        <span class="fab add"><svg viewBox="0 0 16 16"><path d="M8 3v10M3 8h10"/></svg></span>
      </div>
    </div>
  </section>

</main>
</body>
</html>
```